A4 Flyer

Brightwell Care Academy is starting a course in regional Victoria. We are currently advertising (See attached file A34984) in local papers but need to create a one page flyer to distribute to Aged Care facilities in the area. The A4 flyer will be inserted into a folder pack with more detailed information on Brightwell Care Academy. Important to use images and logoes attached

Target Market(s)

Flyer to be distributed to Aged Care facility staff and owners

Industry/Entity Type

Advertising

Font styles to use
Sans Serif

Colors
f37123
ec1f27

Requirements
Must have
• BCA Logo
Some image

```html
<!DOCTYPE html>
<html lang="en">
<head>
<meta charset="utf-8">
<title>Brightwell Care Academy – Fast Track Course Flyer</title>
<link rel="stylesheet" href="https://fonts.googleapis.com/css2?family=Anton&family=Roboto:wght@400;700;900&family=Roboto+Mono:wght@700&display=swap">
<style>
  :root{
    --page-bg:#e9e8e5;
    --paper:#ffffff;
    --grey-light:#f1f1f1;
    --logo-panel:#c8c8c8;
    --orange:#f37123;
    --red:#ec1f27;
    --red-orange:#e4491f;
    --yellow-top:#f8d64a;
    --yellow-bottom:#f2b51b;
    --band-top:#f28a2e;
    --band-bottom:#e0561f;
    --accent-yellow:#ffd83a;
    --ink:#1b1b1b;
    --ink-soft:#4a4a4a;
  }
  *{box-sizing:border-box;margin:0;padding:0}
  html,body{width:1200px;height:1000px;overflow:hidden}
  body{background:var(--page-bg);font-family:"Roboto",Arial,sans-serif;position:relative}

  .flyer{position:absolute;left:270px;top:33px;width:660px;height:934px;background:linear-gradient(180deg,var(--paper) 0%,var(--grey-light) 45%);box-shadow:0 4px 18px rgba(0,0,0,.18);overflow:hidden}

  .photo{position:absolute}
  .photo--student-left{left:0;top:0;width:260px;height:236px;background:linear-gradient(160deg,#d9d4cf 0%,#b9b2ac 55%,#8d8580 100%)}
  .photo--student-right{left:440px;top:0;width:220px;height:236px;background:linear-gradient(200deg,#e6e3e0 0%,#c4bcb6 50%,#6a5e58 100%)}
  .photo--trainer{left:0;top:540px;width:265px;height:260px;background:linear-gradient(135deg,#f2ede6 0%,#d7b8a2 45%,#b4584a 75%,#7d3d34 100%);z-index:2}

  .logo-panel{position:absolute;left:260px;top:0;width:180px;height:236px;background:var(--logo-panel);display:flex;flex-direction:column;align-items:center;justify-content:center;gap:14px;padding:0 14px}
  .logo-mark{width:54px;height:54px;border-radius:50%;background:var(--orange)}
  .logo-name{font-family:"Roboto",Arial,sans-serif;font-weight:700;font-size:22px;line-height:1.1;color:var(--ink-soft);text-align:center}

  .headline{position:absolute;left:24px;top:246px;font-family:"Anton",Impact,sans-serif;font-size:54px;line-height:1;color:var(--red-orange);letter-spacing:.5px;z-index:3}
  .subhead{position:absolute;left:150px;top:310px;font-weight:900;font-size:30px;color:var(--ink);z-index:3}
  .funding{position:absolute;left:24px;top:352px;font-family:"Roboto Mono",monospace;font-size:15px;color:var(--ink);z-index:3}

  .feature-area{position:absolute;left:0;top:410px;width:660px;height:390px;background:linear-gradient(180deg,var(--yellow-top) 0%,var(--yellow-bottom) 100%)}

  .qualification-banner{position:absolute;left:20px;top:386px;width:620px;height:74px;border-radius:14px;background:linear-gradient(180deg,#f0652a 0%,var(--red-orange) 100%);border:3px solid #fff;box-shadow:0 3px 6px rgba(0,0,0,.25);display:flex;align-items:center;justify-content:center;text-align:center;font-family:"Roboto Mono",monospace;font-size:19px;line-height:1.25;color:#fff;z-index:3}

  .venue{position:absolute;left:170px;top:470px;z-index:3}
  .venue__name{font-weight:900;font-size:24px;color:var(--red-orange)}
  .venue__detail{font-size:16px;font-weight:700;color:var(--ink);line-height:1.3}

  .course-units{position:absolute;left:320px;top:548px;list-style:none;z-index:3}
  .course-units li{display:flex;align-items:flex-start;gap:8px;font-weight:700;font-size:18px;color:var(--ink);line-height:1.05;margin-bottom:7px}
  .course-units svg{flex:none;margin-top:2px}

  .start-badge{position:absolute;left:498px;top:560px;width:140px;height:140px;z-index:3}
  .start-badge__text{position:absolute;inset:0;display:flex;flex-direction:column;align-items:center;justify-content:center;font-weight:900;font-size:25px;line-height:1;color:#fff;transform:rotate(-22deg)}

  .enrol-band{position:absolute;left:0;top:800px;width:660px;height:134px;background:linear-gradient(180deg,var(--band-top) 0%,var(--band-bottom) 100%);border-top:4px solid #fff}
  .enrol{position:absolute;left:275px;top:810px;width:370px;text-align:center;z-index:3}
  .enrol__label{font-weight:900;font-size:17px;color:#fff}
  .enrol__web{font-weight:700;font-size:25px;color:var(--accent-yellow);margin-top:4px}
  .enrol__phone{font-weight:900;font-size:26px;color:var(--accent-yellow);margin-top:2px}
  .enrol__note{font-size:9px;color:#fff;margin-top:8px}
</style>
</head>
<body>
<main class="flyer">
  <div class="photo photo--student-left" role="img" aria-label="Photo of a mature male student writing at a classroom desk"></div>
  <div class="logo-panel">
    <span class="logo-mark"></span>
    <span class="logo-name">Brightwell Care Academy</span>
  </div>
  <div class="photo photo--student-right" role="img" aria-label="Photo of a female student smiling at a classroom desk"></div>

  <h1 class="headline">UNIQUE OPPORTUNITY!</h1>
  <h2 class="subhead">Fast Track Course</h2>
  <p class="funding">Government Funding for eligible students! Fees from $117</p>

  <section class="feature-area"></section>

  <div class="qualification-banner">DOUBLE QUALIFICATION - CERT III IN AGED CARE<br>WITH HOME AND COMMUNITY CARE</div>

  <div class="venue">
    <p class="venue__name">Harlow Lodge Nursing</p>
    <p class="venue__detail">Home - Millbrook</p>
    <p class="venue__detail">9:00am - 3:00pm</p>
  </div>

  <div class="photo photo--trainer" role="img" aria-label="Photo of a trainer demonstrating on an anatomy model"></div>

  <ul class="course-units">
    <li><svg width="16" height="14" viewBox="0 0 16 14"><path d="M1 7l5 5L15 1" fill="none" stroke="#ec1f27" stroke-width="3"/></svg>Pathology</li>
    <li><svg width="16" height="14" viewBox="0 0 16 14"><path d="M1 7l5 5L15 1" fill="none" stroke="#ec1f27" stroke-width="3"/></svg>Aged Care</li>
    <li><svg width="16" height="14" viewBox="0 0 16 14"><path d="M1 7l5 5L15 1" fill="none" stroke="#ec1f27" stroke-width="3"/></svg>First Aid</li>
    <li><svg width="16" height="14" viewBox="0 0 16 14"><path d="M1 7l5 5L15 1" fill="none" stroke="#ec1f27" stroke-width="3"/></svg>CPR</li>
    <li><svg width="16" height="14" viewBox="0 0 16 14"><path d="M1 7l5 5L15 1" fill="none" stroke="#ec1f27" stroke-width="3"/></svg>Anaphylaxis</li>
    <li><svg width="16" height="14" viewBox="0 0 16 14"><path d="M1 7l5 5L15 1" fill="none" stroke="#ec1f27" stroke-width="3"/></svg>Home &amp;<br>Community Care</li>
    <li><svg width="16" height="14" viewBox="0 0 16 14"><path d="M1 7l5 5L15 1" fill="none" stroke="#ec1f27" stroke-width="3"/></svg>Medications for PCA's</li>
    <li><svg width="16" height="14" viewBox="0 0 16 14"><path d="M1 7l5 5L15 1" fill="none" stroke="#ec1f27" stroke-width="3"/></svg>Health Services</li>
  </ul>

  <div class="start-badge">
    <svg width="140" height="140" viewBox="0 0 140 140">
      <polygon fill="#e4491f" stroke="#fff" stroke-width="2" points="140,70 128.9,81.7 134.7,96.8 119.9,103.4 119.5,119.5 103.4,119.9 96.8,134.7 81.7,128.9 70,140 58.3,128.9 43.2,134.7 36.6,119.9 20.5,119.5 20.1,103.4 5.3,96.8 11.1,81.7 0,70 11.1,58.3 5.3,43.2 20.1,36.6 20.5,20.5 36.6,20.1 43.2,5.3 58.3,11.1 70,0 81.7,11.1 96.8,5.3 103.4,20.1 119.5,20.5 119.9,36.6 134.7,43.2 128.9,58.3"/>
    </svg>
    <div class="start-badge__text"><span>Start</span><span>July</span><span>2014</span></div>
  </div>

  <footer class="enrol-band"></footer>
  <div class="enrol">
    <p class="enrol__label">TO ENROL VISIT</p>
    <p class="enrol__web">brightwellcare.com.au</p>
    <p class="enrol__phone">OR CALL 9555 0142</p>
    <p class="enrol__note">This training is delivered with VIC and Comm Govt Funding to eligible students</p>
  </div>
</main>
</body>
</html>
```